Need Letterhead and Business Card

I have a logo but i need new letterhead and biz cards. We are a real estate investment firm so we need very professional but also do not want to be old fashioned. We have 3 locations; Singapore, New York and Ponte Vedra Florida. I can provide full addresses if needed. If you have adjustments to our logo you would recommend we are open to them.
I will be putting in a separate project but we also need a template for our own powerpoint slide presentations and website.

Real Estate

```html
<!DOCTYPE html>
<html lang="en">
<head>
<meta charset="utf-8">
<title>Kestrel Stationery</title>
<link href="https://fonts.googleapis.com/css2?family=Marcellus&family=Open+Sans:wght@300;400&display=swap" rel="stylesheet">
<style>
  :root {
    --backdrop: #ececec;
    --paper: #f7f7f7;
    --brand-blue: #2b5f91;
    --card-blue: #245c8c;
    --brand-gold: #b8953f;
    --ink: #555555;
    --ink-dark: #2f2f2f;
    --rule: #cbbd95;
    --signature-tone: #e3e3e3;
  }
  * { margin: 0; padding: 0; box-sizing: border-box; }
  html, body { width: 1200px; height: 1000px; overflow: hidden; }
  body { background: var(--backdrop); font-family: "Open Sans", sans-serif; position: relative; }

  .letterhead {
    position: absolute; left: 137px; top: 98px; width: 583px; height: 818px;
    background: var(--paper); box-shadow: 0 2px 6px rgba(0,0,0,.12);
  }
  .brand { position: absolute; }
  .brand-name {
    font-family: "Marcellus", serif; color: var(--brand-blue);
    letter-spacing: 1px; line-height: 1; display: flex; align-items: center; gap: 6px;
  }
  .brand-dot { display: inline-block; border-radius: 50%; background: var(--brand-blue); }
  .brand-tagline {
    font-family: "Marcellus", serif; color: var(--brand-gold);
    text-transform: uppercase; white-space: nowrap;
  }
  .letterhead .brand { left: 71px; top: 52px; }
  .letterhead .brand-name { font-size: 36px; }
  .letterhead .brand-dot { width: 10px; height: 10px; }
  .letterhead .brand-tagline { font-size: 5.6px; margin-top: 5px; }

  .contact-block { font-family: "Marcellus", serif; font-size: 8px; line-height: 10.5px; color: var(--ink-dark); }
  .contact-block b { color: var(--brand-blue); font-weight: 400; }
  .letterhead .contact-block { position: absolute; left: 414px; top: 72px; }

  .letter-body {
    position: absolute; left: 78px; top: 210px; width: 426px;
    font-size: 9.4px; font-weight: 300; line-height: 15.6px; color: var(--ink);
    text-align: justify;
  }
  .letter-body p { margin-bottom: 15.6px; }
  .signature { position: absolute; left: 128px; top: 585px; width: 135px; height: 32px; }

  .letter-footer { position: absolute; left: 110px; top: 736px; width: 362px; text-align: center; }
  .letter-footer .rule { height: 1px; background: var(--rule); }
  .footer-company { font-family: "Marcellus", serif; font-size: 8.6px; color: var(--brand-blue); margin-top: 10px; text-transform: uppercase; }
  .offices { display: flex; justify-content: space-between; margin-top: 8px; }
  .office { width: 110px; }
  .office-city { font-family: "Marcellus", serif; font-size: 10.5px; color: var(--brand-gold); }
  .office-address { font-family: "Marcellus", serif; font-size: 7px; line-height: 10px; color: var(--ink-dark); margin-top: 2px; }

  .card { position: absolute; width: 236px; height: 156px; box-shadow: 0 2px 5px rgba(0,0,0,.15); }
  .card-front { left: 815px; top: 556px; background: var(--card-blue); }
  .card-front .brand { left: 0; right: 0; top: 50px; text-align: center; }
  .card-front .brand-name { font-size: 30px; color: #ffffff; justify-content: center; }
  .card-front .brand-dot { width: 8px; height: 8px; background: #ffffff; }
  .card-front .brand-tagline { font-size: 5px; color: #e9dcb8; margin-top: 5px; }

  .card-back { left: 809px; top: 757px; width: 240px; height: 158px; background: var(--paper); }
  .card-back .brand { left: 0; right: 0; top: 22px; text-align: center; }
  .card-back .brand-name { font-size: 20px; justify-content: center; }
  .card-back .brand-dot { width: 6px; height: 6px; }
  .card-back .brand-tagline { font-size: 3.6px; margin-top: 3px; }
  .card-locations { position: absolute; left: 0; right: 0; top: 63px; text-align: center; font-family: "Marcellus", serif; font-style: normal; font-size: 8.6px; color: var(--brand-gold); }
  .card-person { position: absolute; left: 24px; top: 114px; }
  .person-name { font-family: "Marcellus", serif; font-size: 11px; color: var(--ink-dark); }
  .person-role { font-family: "Marcellus", serif; font-size: 7.6px; color: var(--brand-gold); }
  .card-back .contact-block { position: absolute; left: 147px; top: 112px; font-size: 6.6px; line-height: 9.5px; }
</style>
</head>
<body>
  <section class="letterhead">
    <div class="brand">
      <div class="brand-name"><span class="brand-dot"></span>KESTREL</div>
      <div class="brand-tagline">Real Estate Investment &amp; Management</div>
    </div>
    <div class="contact-block">
      <div><b>Phone:</b> 555-0100-2468</div>
      <div><b>E-mail:</b> contact@kestrel.sg</div>
      <div><b>Web:</b> www.kestrel.sg</div>
    </div>

    <div class="letter-body">
      <p>Dear &nbsp;Client,</p>
      <p>Lorem ipsum dolor sit amet, consectetur adipiscing elit. Nulla sodales nisi vitae Lorem ipsum dolor sit amet, consectetur adipiscing elit. Suspendisse feugiat eros nisl, a facilisis risus eleifend sed. Aliquam mauris enim, fermentum eu lacinia sit amet, laoreet eu leo. Nullam eleifend nulla in libero tristique, ac vulputate odio tincidunt. Etiam non condimentum tortor. Integer suscipit neque nec odio porttitor cursus. Phasellus a sapien blandit, suscipit justo id, condimentum ante. Morbi tristique justo risus, id mattis dui molestie ut. Nullam volutpat ut quam commodo faucibus. Pellentesque urna est, interdum in elit quis, pharetra elementum orci. Nam pharetra velit molestie justo placerat scelerisque.</p>
      <p>Sed est tellus, rutrum in nisl a, consequat sollicitudin elit. Aliquam vitae vestibulum felis. Morbi iaculis nunc volutpat diam ullamcorper vestibulum. Nulla facilisi. Aenean accumsan gravida orci, vitae consectetur justo aliquet et. Curabitur vehicula tempus dolor, a gravida metus vestibulum sit amet. Integer non erat elementum, malesuada metus vel, fermentum lectus. Etiam sit amet nisl ac augue semper ultrices.</p>
      <p>Nulla tincidunt molestie libero vel pretium. Donec condimentum nulla sit amet risus semper imperdiet. Duis congue eros nec diam blandit, et pellentesque sapien auctor.</p>
      <p>Best regards.</p>
    </div>

    <svg class="signature" role="img" aria-label="Handwritten signature of the sender" viewBox="0 0 135 32">
      <rect width="135" height="32" rx="4" fill="var(--signature-tone)"/>
    </svg>

    <footer class="letter-footer">
      <div class="rule"></div>
      <div class="footer-company">Kestrel Real Estate Investment &amp; Management</div>
      <div class="offices">
        <div class="office">
          <div class="office-city">Singapore</div>
          <div class="office-address">123, Main Fake Street,<br>Anytown, Postal Code.</div>
        </div>
        <div class="office">
          <div class="office-city">New York</div>
          <div class="office-address">123, Main Fake Street,<br>Anytown, Postal Code.</div>
        </div>
        <div class="office">
          <div class="office-city">Florida</div>
          <div class="office-address">123, Main Fake Street,<br>Anytown, Postal Code.</div>
        </div>
      </div>
    </footer>
  </section>

  <section class="card card-front">
    <div class="brand">
      <div class="brand-name"><span class="brand-dot"></span>KESTREL</div>
      <div class="brand-tagline">Real Estate Investment &amp; Management</div>
    </div>
  </section>

  <section class="card card-back">
    <div class="brand">
      <div class="brand-name"><span class="brand-dot"></span>KESTREL</div>
      <div class="brand-tagline">Real Estate Investment &amp; Management</div>
    </div>
    <div class="card-locations">Singapore &nbsp;•&nbsp; New York &nbsp;•&nbsp; Florida</div>
    <div class="card-person">
      <div class="person-name">Daniel Reyes</div>
      <div class="person-role">Managing Partner</div>
    </div>
    <div class="contact-block">
      <div><b>Phone:</b> 555-0100-2468</div>
      <div><b>E-mail:</b> contact@kestrel.sg</div>
      <div><b>Web:</b> www.kestrel.sg</div>
    </div>
  </section>
</body>
</html>
```